Harbor Kestrel
Your Trusted Advisors
Professional
Rosalind Okafor
Partner
418 Tamarack Lane
Phoenixville, PA 19388
rosalind.okafor@harborkestrel.co
www.harborkestrel.co

```html
<!DOCTYPE html>
<html lang="en">
<head>
<meta charset="utf-8">
<title>Harbor Kestrel Stationery</title>
<link rel="stylesheet" href="https://fonts.googleapis.com/css2?family=Open+Sans:wght@400;600;700;800&display=swap">
<style>
:root{
  --red:#c8102e;
  --dark:#2a2a2c;
  --ink:#3a3a3a;
  --muted:#8a8a8a;
  --line:#c9c9c9;
  --paper:#ffffff;
  --stage:#e7e5e2;
}
*{box-sizing:border-box;margin:0;padding:0}
html,body{width:1200px;height:559px;overflow:hidden}
body{background:var(--stage);font-family:"Open Sans",Arial,sans-serif;color:var(--ink);position:relative}
.sheet,.envelope,.card{position:absolute;background:var(--paper);box-shadow:0 2px 6px rgba(0,0,0,.18)}
.brand{display:flex;align-items:center;gap:4px;font-weight:800;color:var(--red);text-transform:uppercase;letter-spacing:.2px;line-height:1}
.brand-dot{width:7px;height:7px;border-radius:50%;background:var(--red);flex:none}
.brand.light{color:#fff}
.brand.light .brand-dot{background:#fff}
.contact{font-size:4.6px;line-height:1.55;color:var(--ink)}
.contact a{color:var(--red);text-decoration:none}

/* Fax sheet */
.fax{left:12px;top:10px;width:214px;height:539px;padding:16px 16px}
.fax .brand{font-size:9px}
.fax .contact{position:absolute;right:16px;top:16px;text-align:left}
.fax-title{font-size:19px;font-weight:800;color:var(--dark);margin:26px 0 10px}
.fax-form{display:grid;grid-template-columns:1fr 1fr;column-gap:12px;row-gap:9px;font-size:5px;font-weight:600}
.field{display:flex;align-items:flex-end;gap:3px}
.field span{flex:1;border-bottom:.6px solid var(--line);height:6px}
.fax-rule{border-top:1px solid var(--dark);margin:12px 0 6px}
.checks{display:flex;justify-content:space-between;font-size:4.4px}
.checks label{display:flex;align-items:center;gap:2px}
.checks i{width:4px;height:4px;border:.6px solid var(--ink);display:inline-block}

/* Letterhead */
.letter{left:236px;top:10px;width:228px;height:539px;padding:16px 18px}
.letter .brand{font-size:9px}
.letter .contact{position:absolute;right:18px;top:16px}
.letter-body{margin-top:34px;font-size:4.7px;line-height:1.65;color:#555}
.letter-body p{margin-bottom:7px}
.signature{width:52px;height:14px;margin:6px 0 4px;background:linear-gradient(90deg,#d9d9d9,#f3f3f3)}
.letter-foot{position:absolute;left:0;right:0;bottom:0;height:5px;background:linear-gradient(90deg,var(--red) 60%,var(--dark) 60%)}

/* Envelopes */
.envelope{width:330px;height:158px}
.env-front{left:484px;top:20px;padding:14px 16px}
.env-front .brand{font-size:10px}
.env-front .contact{margin-top:6px}
.env-recipient{position:absolute;left:150px;top:82px;width:120px}
.env-recipient span{display:block;height:1px;background:var(--line);margin-bottom:8px}
.env-back{left:848px;top:20px;overflow:hidden}
.env-back svg{position:absolute;inset:0}
.env-back .brand{position:absolute;left:0;right:0;top:50px;justify-content:center;font-size:11px}

/* Business cards */
.card{width:236px;height:132px}
.card-dark{background:var(--dark);display:flex;align-items:center;justify-content:center}
.card-dark .brand{font-size:13px}
.card-light{padding:16px 18px}
.card-light .brand{font-size:10px}
.card-name{font-size:9px;font-weight:700;color:var(--dark);margin-top:22px}
.card-role{font-size:6px;color:var(--red);font-weight:600;margin-bottom:8px}
.card-light .contact{font-size:5.6px}
.card-band{position:absolute;left:0;right:0;bottom:0;height:6px;background:var(--red)}
.c1{left:560px;top:226px}
.c2{left:812px;top:226px}
.c3{left:560px;top:380px}
.c4{left:812px;top:380px}
.tagline{font-size:5.5px;color:#bbb;margin-top:4px;text-align:center;letter-spacing:.6px}
.card-dark .stack{display:flex;flex-direction:column;align-items:center}
</style>
</head>
<body>

<section class="sheet fax">
  <div class="brand"><span class="brand-dot"></span>Harbor Kestrel</div>
  <div class="contact">418 Tamarack Lane<br>Phoenixville, PA 19388<br><a>www.harborkestrel.co</a></div>
  <h1 class="fax-title">FAX</h1>
  <div class="fax-form">
    <div class="field">To:<span></span></div><div class="field">From:<span></span></div>
    <div class="field">Fax:<span></span></div><div class="field">Pages:<span></span></div>
    <div class="field">Phone:<span></span></div><div class="field">Date:<span></span></div>
    <div class="field">Re:<span></span></div><div class="field">CC:<span></span></div>
  </div>
  <div class="fax-rule"></div>
  <div class="checks">
    <label><i></i>Urgent</label><label><i></i>For Review</label><label><i></i>Please Comment</label><label><i></i>Please Reply</label><label><i></i>Please Recycle</label>
  </div>
</section>

<section class="sheet letter">
  <div class="brand"><span class="brand-dot"></span>Harbor Kestrel</div>
  <div class="contact">418 Tamarack Lane<br>Phoenixville, PA 19388<br><a>www.harborkestrel.co</a></div>
  <div class="letter-body">
    <p>March 4, 2024</p>
    <p>Dear Client,<br>Re: Advisory Proposal</p>
    <p>Thank you for meeting with our team last week. We value the chance to review your plans and share how our advisors can support your goals in the year ahead.</p>
    <p>Our proposal outlines clear steps, a simple timeline and regular check-ins so you always know where things stand. Each stage is handled by a partner who knows your needs well.</p>
    <p>Please review the enclosed summary and call us with any questions. We look forward to working together.</p>
    <p>Sincerely,</p>
    <div class="signature" role="img" aria-label="Handwritten signature"></div>
    <p>Rosalind Okafor<br>Partner</p>
  </div>
  <div class="letter-foot"></div>
</section>

<section class="envelope env-front">
  <div class="brand"><span class="brand-dot"></span>Harbor Kestrel</div>
  <div class="contact">418 Tamarack Lane<br>Phoenixville, PA 19388<br><a>www.harborkestrel.co</a></div>
  <div class="env-recipient"><span></span><span></span><span></span></div>
</section>

<section class="envelope env-back">
  <svg width="330" height="158" viewBox="0 0 330 158">
    <polygon points="0,0 330,0 165,78" fill="var(--red)"/>
    <polyline points="0,158 165,90 330,158" fill="none" stroke="#e2e2e2" stroke-width="1"/>
  </svg>
  <div class="brand light" style="top:22px"><span class="brand-dot"></span>Harbor Kestrel</div>
</section>

<section class="card card-dark c1">
  <div class="stack"><div class="brand light"><span class="brand-dot"></span>Harbor Kestrel</div><div class="tagline">YOUR TRUSTED ADVISORS</div></div>
</section>
<section class="card card-light c2">
  <div class="brand"><span class="brand-dot"></span>Harbor Kestrel</div>
  <div class="card-name">Rosalind Okafor</div>
  <div class="card-role">Partner</div>
  <div class="contact">418 Tamarack Lane, Phoenixville, PA 19388<br>rosalind.okafor@harborkestrel.co<br><a>www.harborkestrel.co</a></div>
  <div class="card-band"></div>
</section>
<section class="card card-light c3">
  <div class="brand"><span class="brand-dot"></span>Harbor Kestrel</div>
  <div class="card-name">Rosalind Okafor</div>
  <div class="card-role">Professional</div>
  <div class="contact">418 Tamarack Lane, Phoenixville, PA 19388<br>rosalind.okafor@harborkestrel.co<br><a>www.harborkestrel.co</a></div>
  <div class="card-band"></div>
</section>
<section class="card card-dark c4">
  <div class="stack"><div class="brand light"><span class="brand-dot"></span>Harbor Kestrel</div><div class="tagline">YOUR TRUSTED ADVISORS</div></div>
</section>

</body>
</html>
```